Bramble Roofing Website Relaunch

We require a re-launch of our website, We are a longrun roofing company based in New Zealand, we are rapidly expanding and require a more professionally presented website our current website is www.brambleroofing.co.nz we want something modern, masculine and communicates a "strong" "superior" image, we already have a logo which I have attached we use the orange and silver one as you will see on our current website

Industry/Entity Type

It Company

Number of Pages Required

1 page

Colors
f37122
f78f20
000000
1b1b1b
474747
d3d3d3
f5f5f5

Requirements
Must have
• Images of our work
• Email and Mobile Contact Details
• Link to Facebook page
• Who We Are, What We Do
• Certified Trade Craftsman Logo
• Our Logo

```html
<!DOCTYPE html>
<html lang="en">
<head>
<meta charset="utf-8">
<title>Bramble Roofing — Long Run Roofing Specialists</title>
<link rel="stylesheet" href="https://fonts.googleapis.com/css2?family=Poppins:wght@300;400;500;600;700&display=swap">
<style>
:root{
  --orange:#f37122;
  --orange-light:#f78f20;
  --black:#000000;
  --ink:#1b1b1b;
  --charcoal:#474747;
  --silver:#d3d3d3;
  --mist:#f5f5f5;
  --panel:#ececec;
  --text:#6b6b6b;
  --white:#ffffff;
}
*{margin:0;padding:0;box-sizing:border-box}
html,body{width:1200px;height:3141px;overflow:hidden}
body{position:relative;font-family:'Poppins',sans-serif;color:var(--ink);background:var(--white)}
.abs{position:absolute}
a{color:inherit;text-decoration:none}

/* Hero */
.hero{left:0;top:0;width:1200px;height:576px}
.hero svg{position:absolute;left:0;top:0}
.topline{font-size:12px;color:var(--white);font-weight:600;top:23px}
.topline span{font-weight:400}
.nav{top:64px;display:flex;font-size:11.5px;color:var(--white)}
.nav a{padding:0 0 9px}
.nav .sep{margin:0 26px;opacity:.7}
.nav-left{left:155px;width:305px;border-bottom:1px solid rgba(255,255,255,.45)}
.nav-left a.active{color:var(--orange);border-bottom:2px solid var(--orange)}
.nav-right{left:740px;width:205px;border-bottom:1px solid rgba(255,255,255,.45)}
.brand{left:0;width:1200px;top:40px;display:flex;align-items:center;justify-content:center;gap:12px;color:var(--white);font-weight:600;font-size:19px;letter-spacing:.5px}
.brand i{display:block;width:30px;height:30px;border:3px solid var(--silver);transform:rotate(45deg)}
.btn-quote{left:946px;top:57px;width:122px;height:31px;background:var(--orange);color:var(--white);font-size:10.5px;font-weight:600;display:flex;align-items:center;justify-content:center;letter-spacing:.5px}
.hero-title{left:0;width:1200px;top:225px;text-align:center;color:var(--white);font-size:33px;font-weight:300}
.hero-title b{font-weight:600}
.hero-sub{left:0;width:1200px;top:280px;text-align:center;color:var(--white);font-size:15px;line-height:22px}
.btn-explore{left:536px;top:348px;width:128px;height:32px;background:var(--orange);color:var(--white);font-size:10.5px;font-weight:600;display:flex;align-items:center;justify-content:center}
.diamond{width:26px;height:26px;transform:rotate(45deg);background:rgba(255,255,255,.55)}

/* About */
.about{left:0;top:576px;width:1200px;height:448px;background:var(--panel)}
.eyebrow{font-size:11px;color:var(--ink)}
.sec-title{font-size:25px;color:var(--ink);font-weight:400}
.sec-title b{font-weight:600}
.about-panel{left:534px;top:123px;width:509px;height:260px;background:var(--mist)}
.about-text{left:664px;top:182px;width:326px;font-size:11.5px;line-height:18px;color:var(--text)}
.btn-outline{border:1px solid var(--orange);color:var(--ink);font-size:10px;font-weight:500;display:flex;align-items:center;justify-content:center;letter-spacing:.5px;background:var(--white)}

/* Services */
.centered{left:0;width:1200px;text-align:center}
.service-title{font-size:19px;font-weight:600;letter-spacing:1px;text-align:center}
.service-text{font-size:11.5px;line-height:18px;color:var(--text);text-align:center}
.service-text b{color:var(--ink);font-weight:600}
.read-more{font-size:10px;font-weight:500;text-align:center}

/* Work */
.work-band{left:0;top:1702px;width:1200px;height:116px}
.work-overlay{left:467px;top:1826px;width:237px;height:188px;background:var(--orange);color:var(--white);text-align:center}

/* Testimonial */
.quote-text{left:200px;width:800px;top:2321px;text-align:center;font-size:16px;line-height:24.5px;color:var(--charcoal)}
.avatar{left:567px;top:2442px;width:66px;height:66px;border-radius:50%;background:linear-gradient(#cfcfcf,#9a9a9a);border:3px solid var(--white);box-shadow:0 0 0 1px var(--silver)}
.dot{width:5px;height:5px;border-radius:50%;background:var(--orange);top:2586px}

/* Contact */
.signup{left:0;top:2660px;width:601px;height:268px;background:var(--charcoal);color:var(--white)}
.contact{left:601px;top:2660px;width:599px;height:238px;background:var(--panel)}
.contact-row{left:664px;font-size:12px;color:var(--charcoal)}
.contact-row b{color:var(--ink);font-weight:600;margin-right:12px}

/* Footer */
.footer{left:0;top:2898px;width:1200px;height:243px;background:var(--ink)}
.foot-nav{top:2990px;left:410px;display:flex;gap:34px;font-size:12.5px;color:var(--silver)}
.foot-nav .active{color:var(--orange)}
.social{width:27px;height:27px;border-radius:50%;background:var(--silver);top:2985px}
</style>
</head>
<body>

<!-- HERO -->
<section class="abs hero">
  <svg width="1200" height="576" viewBox="0 0 1200 576">
    <defs>
      <linearGradient id="heroSky" x1="0" y1="0" x2="0" y2="1">
        <stop offset="0" stop-color="#33485e"/>
        <stop offset=".45" stop-color="#5d6f80"/>
        <stop offset=".7" stop-color="#525a4e"/>
        <stop offset="1" stop-color="#45493f"/>
      </linearGradient>
    </defs>
    <rect width="1200" height="576" fill="var(--panel)"/>
    <polygon role="img" aria-label="Steel frame of a commercial building under construction at dusk" points="0,0 1200,0 1200,430 600,576 0,430" fill="url(#heroSky)"/>
  </svg>
  <div class="abs topline" style="left:155px">Email: <span>brambleroofing@kiwimail.co.nz</span></div>
  <div class="abs topline" style="left:894px">Call Us: <span>&#9742; 021 555 01842</span></div>
  <nav class="abs nav nav-left"><a class="active">Home</a><span class="sep">|</span><a>About Us</a><span class="sep">|</span><a>Services</a></nav>
  <div class="abs brand"><i></i>Bramble Roofing</div>
  <nav class="abs nav nav-right"><a>Our Work</a><span class="sep">|</span><a>Contact</a></nav>
  <a class="abs btn-quote">GET A QUOTE</a>
  <h1 class="abs hero-title">Long Run <b>Roofing Specialists</b></h1>
  <p class="abs hero-sub">We are a local, family owned and operated company with over 18 years<br>extensive experienc in the roofing industry.</p>
  <a class="abs btn-explore">EXPLORE MORE</a>
  <div class="abs diamond" style="left:52px;top:295px"></div>
  <div class="abs diamond" style="left:1120px;top:295px;background:rgba(243,113,34,.6)"></div>
  <svg class="abs" style="left:582px;top:520px" width="36" height="36" viewBox="0 0 36 36"><rect x="6" y="6" width="24" height="24" transform="rotate(45 18 18)" fill="none" stroke="var(--orange)" stroke-width="2.5"/><rect x="13" y="13" width="10" height="10" transform="rotate(45 18 18)" fill="var(--orange)"/></svg>
</section>

<!-- ABOUT -->
<section class="abs about">
  <div class="abs about-panel"></div>
  <div class="abs" style="left:565px;top:115px;width:46px;height:237px;background:var(--orange)"></div>
  <div class="abs" role="img" aria-label="Dark weatherboard house with new roof on a green lawn" style="left:155px;top:69px;width:446px;height:272px;background:linear-gradient(#8fb3d6 0%,#bcd0e0 38%,#2b2d31 52%,#3b3b3b 62%,#4f8a2c 70%,#3f7424 100%)"></div>
  <div class="abs" role="img" aria-label="Modern house with dark cladding at dusk" style="left:230px;top:236px;width:283px;height:147px;border:4px solid var(--white);background:linear-gradient(#7a8aa0 0%,#9aa4ae 40%,#2f2f2f 60%,#4a4036 100%)"></div>
  <div class="abs eyebrow" style="left:664px;top:91px">Who We Are</div>
  <h2 class="abs sec-title" style="left:664px;top:106px">About <b>BRAMBLE</b></h2>
  <div class="abs" style="left:790px;top:128px;width:120px;height:1px;background:var(--silver)"></div>
  <p class="abs about-text">We are a local, family owned and operated company with over 18 years extensive experience in the roofing industry. Roofing not only Waikato and Auckland but surrounding areas also. We are committed to providing superior service...</p>
  <a class="abs btn-outline" style="left:664px;top:297px;width:128px;height:32px">DISCOVER MORE</a>
</section>

<!-- SERVICES -->
<section>
  <div class="abs eyebrow centered" style="top:1085px">What We Do</div>
  <h2 class="abs sec-title centered" style="top:1100px">Our <b>Services</b></h2>
  <svg class="abs" style="left:150px;top:1170px" width="900" height="340" viewBox="0 0 900 340">
    <defs>
      <linearGradient id="resPhoto" x1="0" y1="0" x2="0" y2="1"><stop offset="0" stop-color="#b9cde0"/><stop offset=".4" stop-color="#d2dde6"/><stop offset=".48" stop-color="#2c2d30"/><stop offset=".62" stop-color="#3a3a3a"/><stop offset=".66" stop-color="#4d8a2b"/><stop offset="1" stop-color="#3c7222"/></linearGradient>
      <linearGradient id="comPhoto" x1="0" y1="0" x2="0" y2="1"><stop offset="0" stop-color="#2f6fc0"/><stop offset=".45" stop-color="#6f9ed4"/><stop offset=".6" stop-color="#7b8a8c"/><stop offset=".72" stop-color="#6f8a4a"/><stop offset=".78" stop-color="#a0a3a3"/><stop offset="1" stop-color="#8e9090"/></linearGradient>
    </defs>
    <polygon points="320,316 451,316 451,330 310,330" fill="var(--orange)"/>
    <polygon role="img" aria-label="Residential home with dark long run roof" points="70,3 451,3 451,300 432,323 7,323 7,160" fill="url(#resPhoto)"/>
    <polygon points="862,200 900,200 886,330 818,330" fill="var(--orange)"/>
    <polygon role="img" aria-label="Commercial steel frame building against blue sky" points="505,3 893,3 838,323 443,323" fill="url(#comPhoto)"/>
  </svg>
  <div class="abs service-title" style="left:223px;width:300px;top:1518px">Residential</div>
  <p class="abs service-text" style="left:203px;width:340px;top:1555px">At Bramble Roofing we offer a variety of professional services specializing in <b>Residential</b> Industrial Long Run Roofing Installations New Roofs and...</p>
  <div class="abs read-more" style="left:273px;width:200px;top:1626px">READ MORE &rarr;</div>
  <div class="abs service-title" style="left:665px;width:300px;top:1518px">Commercial</div>
  <p class="abs service-text" style="left:645px;width:340px;top:1555px">At Bramble Roofing we offer a variety of professional services specializing in <b>Commercial</b> Industrial Long Run Roofing Installations New Roofs and...</p>
  <div class="abs read-more" style="left:715px;width:200px;top:1626px;color:var(--orange)">READ MORE &rarr;</div>
</section>

<!-- OUR WORK -->
<section>
  <svg class="abs work-band" width="1200" height="116" viewBox="0 0 1200 116"><rect width="1200" height="116" fill="var(--mist)"/><polygon points="1030,0 1200,0 1200,116 1148,116" fill="#e6e6e6"/></svg>
  <div class="abs eyebrow" style="left:155px;top:1732px">Recent Projects</div>
  <h2 class="abs sec-title" style="left:155px;top:1746px">Our <b>Work</b></h2>
  <a class="abs btn-outline" style="left:898px;top:1744px;width:145px;height:34px;background:transparent">VIEW ALL PROJECTS</a>
  <div class="abs" role="img" aria-label="Long run roof sheets being installed on a large building" style="left:0;top:1818px;width:459px;height:398px;background:linear-gradient(160deg,#8fb2d3 0%,#c6d6e2 30%,#6b7a5a 42%,#3a4350 55%,#23272e 100%)"></div>
  <div class="abs" role="img" aria-label="Residential roofing project" style="left:459px;top:1818px;width:253px;height:203px;background:linear-gradient(#9fb6cc,#4a4a44)"></div>
  <div class="abs work-overlay">
    <div style="font-size:17px;font-weight:500;margin-top:52px">Residential</div>
    <div style="font-size:12px;opacity:.9">Contrary to popular belief</div>
    <svg width="20" height="20" viewBox="0 0 20 20" style="margin-top:20px"><path d="M4 16 L16 4 M10 4 H16 V10 M4 10 V16 H10" stroke="#fff" stroke-width="2" fill="none"/></svg>
  </div>
  <div class="abs" role="img" aria-label="Dark house with new roof on green lawn" style="left:712px;top:1818px;width:255px;height:203px;background:linear-gradient(#4f8fd6 0%,#b9d0e4 38%,#2a2b2e 55%,#3b3b3b 68%,#4b8f2c 74%,#3e7a22 100%)"></div>
  <div class="abs" role="img" aria-label="Modern home with dark cladding" style="left:459px;top:2021px;width:508px;height:195px;background:linear-gradient(#8c9aa8 0%,#a8aeb0 30%,#3a3632 55%,#5a4a3a 100%)"></div>
  <div class="abs" role="img" aria-label="Steel frame commercial building on gravel site" style="left:967px;top:1818px;width:233px;height:398px;background:linear-gradient(#2f77c8 0%,#8ab2dc 40%,#7e8d83 58%,#a3a6a4 72%,#8a8c8c 100%)"></div>
</section>

<!-- TESTIMONIAL -->
<section>
  <div class="abs centered" style="top:2272px;font-size:40px;color:var(--orange);font-weight:700;line-height:40px">&ldquo;</div>
  <p class="abs quote-text">It is a long established fact that a reader will be distracted<br>by the readable content of a page when looking at its layout&nbsp; The point of using<br>Ipsum is that it has a more-or-less normal distribution of lettersit look like<br>readable English on a related project.</p>
  <div class="abs" style="left:459px;top:2461px;font-size:20px;color:var(--silver)">&lsaquo;</div>
  <div class="abs" style="left:731px;top:2461px;font-size:20px;color:var(--orange)">&rsaquo;</div>
  <div class="abs avatar" role="img" aria-label="Client portrait"></div>
  <div class="abs centered" style="top:2526px;font-size:12.5px;color:var(--orange);font-weight:500">Marcus Hale</div>
  <div class="abs centered" style="top:2547px;font-size:9.5px;color:var(--text);letter-spacing:.5px">CEO, RETAIL STORE</div>
  <div class="abs dot" style="left:541px"></div>
  <div class="abs dot" style="left:569px"></div>
  <div class="abs" style="left:594px;top:2582px;width:13px;height:13px;border:1.5px solid var(--orange);border-radius:50%"></div>
  <div class="abs dot" style="left:598px"></div>
  <div class="abs dot" style="left:626px"></div>
  <div class="abs dot" style="left:654px"></div>
</section>

<!-- SIGN UP / CONTACT -->
<section>
  <div class="abs signup"></div>
  <div class="abs contact"></div>
  <h3 class="abs" style="left:155px;top:2706px;font-size:19px;color:var(--white);font-weight:400">Sign <b style="font-weight:600">Up</b></h3>
  <p class="abs" style="left:155px;top:2748px;font-size:12px;line-height:19px;color:var(--white)">Get updated About New things from Us?<br>Join our newsletter</p>
  <div class="abs" style="left:155px;top:2830px;font-size:10.5px;color:var(--silver);font-style:italic">Enter Your Email..</div>
  <div class="abs" style="left:155px;top:2851px;width:285px;height:1px;background:var(--silver)"></div>
  <a class="abs" style="left:440px;top:2821px;width:96px;height:31px;background:var(--orange);color:var(--white);font-size:10.5px;font-weight:600;display:flex;align-items:center;justify-content:center">SUBMIT</a>
  <h3 class="abs" style="left:664px;top:2706px;font-size:19px;font-weight:400">Contact <b style="font-weight:600">Us</b></h3>
  <div class="abs contact-row" style="top:2749px;width:330px;line-height:19px"><b>Address:</b>4410 Harbourview Rd, Hamilton,<br>WK 3204</div>
  <div class="abs contact-row" style="top:2802px"><b>Phone:</b>021 555 01842</div>
  <div class="abs contact-row" style="top:2838px"><b>Email:</b><span style="text-decoration:underline">brambleroofing@kiwimail.co.nz</span></div>
</section>

<!-- FOOTER -->
<footer>
  <div class="abs footer"></div>
  <div class="abs" style="left:1121px;top:2882px;width:28px;height:28px;background:var(--orange);transform:rotate(45deg)"></div>
  <div class="abs" style="left:160px;top:2981px;display:flex;align-items:center;gap:14px;color:var(--silver);font-size:18px;font-weight:600">
    <i style="display:block;width:30px;height:30px;border:3px solid var(--orange);transform:rotate(45deg)"></i>Bramble Roofing
  </div>
  <nav class="abs foot-nav"><a class="active">Home</a><a>About Us</a><a>Services</a><a>Our Work</a><a>Contact us</a></nav>
  <a class="abs social" style="left:898px;background:var(--orange)" aria-label="Social link one"></a>
  <a class="abs social" style="left:934px" aria-label="Social link two"></a>
  <a class="abs social" style="left:970px" aria-label="Social link three"></a>
  <a class="abs social" style="left:1006px" aria-label="Social link four"></a>
  <div class="abs" style="left:155px;top:3066px;width:815px;height:1px;background:#333"></div>
  <div class="abs" role="img" aria-label="Certified Trade Craftsman badge" style="left:976px;top:3046px;width:64px;height:64px;border-radius:50%;background:#2a2a2a;border:2px solid var(--silver)"></div>
  <div class="abs" style="left:155px;top:3094px;font-size:11px;color:#8a8a8a">&copy; 2017 <span style="color:var(--orange)">Bramble Roofing</span>. All Rights reserved.</div>
</footer>

</body>
</html>
```